Letterhead Design Project

Consulting Company , we want a letterhead incorporating both the picture provided and the logo provided. The font name is monotype corsiva.
Target Market(s)
Dentist
Industry/Entity Type
Consulting
Font styles to use
Other font styles liked:
- monotype corsiva

Colors
0455a3
Requirements
Must have
- the logo, the picture (see attached), the website name, the email. and the phone numbers.
- Website: www.tkregulatoryadvisors.solutions
- Email: will be provided to the winner, please use placeholder
- Phone numbers:
- Rhea Lindqvist 5824417093
- Omar Kettering 6148072356

Nice to have
- a swoop or wave across the bottom. a line up the side. I don't know guys. design something unique and professional.

Should not have
- arrows pointing off the logo or anywhere. no arrows. our logo altered in anyway. no broken circles. no variences in blue. we like our logo the way it is. the font is monotype corsiva

```html
<!DOCTYPE html>
<html lang="en">
<head>
<meta charset="utf-8">
<title>TK Regulatory Advisors – Letterhead</title>
<link rel="stylesheet" href="https://fonts.googleapis.com/css2?family=Cormorant+Garamond:ital,wght@1,500;1,600&family=Open+Sans:wght@400;600&display=swap">
<style>
  :root {
    --brand-blue: #3a8fcb;
    --band-grey: #5f6062;
    --panel-grey: #727375;
    --paper: #f4f4f5;
    --body-text: #5a5a5c;
    --stage: #e3e4e6;
    --white: #ffffff;
  }
  * { box-sizing: border-box; margin: 0; padding: 0; }
  html, body { width: 1200px; height: 800px; overflow: hidden; }
  body {
    background: var(--stage);
    font-family: "Open Sans", Arial, sans-serif;
    position: relative;
  }
  .letterhead {
    position: absolute;
    left: 330px; top: 18px;
    width: 540px; height: 764px;
    background: var(--paper);
    overflow: hidden;
    box-shadow: 0 4px 18px rgba(0,0,0,.12);
  }

  /* Header / brand */
  .brand { position: absolute; left: 22px; top: 18px; display: flex; align-items: center; gap: 10px; }
  .brand-dot {
    width: 38px; height: 38px; border-radius: 50%;
    border: 3px solid var(--brand-blue); background: var(--white);
  }
  .brand-name { font-size: 15px; font-weight: 600; color: var(--band-grey); }
  .brand-address {
    position: absolute; left: 72px; top: 44px;
    font-family: "Cormorant Garamond", Georgia, serif; font-style: italic; font-weight: 500;
    font-size: 11px; line-height: 1.3; color: var(--band-grey);
  }
  .header-rules { position: absolute; left: 62px; top: 76px; }

  /* Contact panel */
  .contact-panel {
    position: absolute; left: 340px; top: 92px;
    width: 200px; height: 76px;
    background: var(--panel-grey);
    border-radius: 12px 0 0 12px;
    padding: 8px 0 0 16px;
    color: var(--white);
  }
  .contact-name {
    font-family: "Cormorant Garamond", Georgia, serif; font-style: italic; font-weight: 600;
    font-size: 14px; line-height: 1.05;
  }
  .contact-phone { font-size: 8px; margin: 1px 0 5px 4px; letter-spacing: .3px; }
  .side-band { position: absolute; right: 0; top: 168px; width: 70px; height: 62px; background: var(--brand-blue); }
  .portrait {
    position: absolute; left: 428px; top: 140px;
    width: 88px; height: 88px; border-radius: 50%;
    border: 4px solid var(--white);
    box-shadow: 0 0 0 3px var(--panel-grey);
    background: radial-gradient(circle at 50% 40%, #d9b7a0 0%, #8a6a58 45%, #3b3b3d 100%);
  }

  /* Body copy */
  .letter-body {
    position: absolute; left: 40px; right: 40px; top: 242px;
    font-size: 7.6px; line-height: 1.45; color: var(--body-text);
  }
  .letter-body p { margin-bottom: 7px; }

  /* Footer */
  .footer-web {
    position: absolute; left: 0; top: 632px; width: 350px; height: 64px;
    background: var(--band-grey);
    clip-path: polygon(0 0, 100% 0, 84% 100%, 0 100%);
    color: var(--white); font-size: 11px;
    display: flex; flex-direction: column; align-items: flex-start; justify-content: center;
    padding-left: 40px; gap: 3px;
  }
  .footer-mail {
    position: absolute; left: 262px; right: 0; top: 702px; height: 62px;
    background: var(--brand-blue);
    clip-path: polygon(8% 0, 100% 0, 100% 100%, 0 100%);
    color: var(--white); font-size: 11px;
    display: flex; flex-direction: column; align-items: center; justify-content: center; gap: 3px;
  }
  .footer-icon { display: block; }
  .footer-web .footer-icon { margin-left: 88px; }
</style>
</head>
<body>
  <main class="letterhead">
    <header>
      <div class="brand">
        <span class="brand-dot"></span>
        <span class="brand-name">TK Regulatory Advisors, LLC</span>
      </div>
      <p class="brand-address">418 Alder Lane<br>Brookhaven, Ohio 43017</p>
      <svg class="header-rules" width="300" height="10" viewBox="0 0 300 10" aria-hidden="true">
        <line x1="0" y1="5" x2="300" y2="5" stroke="var(--brand-blue)" stroke-width="2.5"/>
      </svg>

      <section class="contact-panel">
        <p class="contact-name">Rhea Lindqvist</p>
        <p class="contact-phone">582 441 7093</p>
        <p class="contact-name">Omar Kettering</p>
        <p class="contact-phone">614 807 2356</p>
      </section>
      <div class="side-band"></div>
      <div class="portrait" role="img" aria-label="Portrait photograph of the consultant"></div>
    </header>

    <article class="letter-body">
      <p>Lorem ipsum dolor sit amet, consectetur adipiscing elit. Integer aliquam ex eu nibh feugiat, sit amet sagittis felis consectetur. Quisque sit amet urna lobortis, consectetur metus volutpat, sagittis ipsum. Aliquam ornare feugiat sollicitudin. Etiam fermentum suscipit mauris hendrerit placerat.</p>
      <p>Lorem ipsum dolor sit amet, consectetur adipiscing elit. In ac pharetra nibh. Pellentesque elementum ligula id tincidunt aliquam, mi ante tincidunt velit, sed sagittis justo sapien a lorem. Phasellus eu tortor nec lorem tristique convallis. Maecenas luctus lorem luctus pulvinar luctus. Nulla viverra mi ac nisl gravida, vel vehicula lectus hendrerit. Praesent et metus fringilla magna gravida tincidunt.</p>
      <p>Praesent dui sapien, mollis eget risus nec, finibus posuere tortor. Sed lacinia tincidunt ex, eget tristique nunc consequat nec. Pellentesque mollis aliquam fermentum. Cras dolor nisl, aliquet et imperdiet nec, cursus id mauris. In erat risus, commodo sed ex a, facilisis fermentum dolor. Phasellus quam eros, posuere non lobortis a, aliquam et sapien.</p>
      <p>Aenean neque erat, sodales sed egestas sed, sollicitudin sit amet neque. Phasellus commodo tincidunt diam, a maximus urna aliquet nec. Suspendisse sit amet euismod lorem. Vestibulum condimentum placerat pellentesque. Etiam eu dui at arcu vehicula hendrerit in quis magna.</p>
      <p>In id egestas arcu. Morbi accumsan, enim et viverra malesuada, dolor massa gravida eros, a venenatis risus risus eget arcu. Nullam lacinia, nibh ac vestibulum consequat, leo turpis pharetra orci, vel malesuada lectus ligula eget metus. Vestibulum ante ipsum primis in faucibus orci luctus et ultrices posuere cubilia curae.</p>
    </article>

    <footer>
      <div class="footer-web">
        <svg class="footer-icon" width="13" height="13" viewBox="0 0 24 24" aria-hidden="true" fill="none" stroke="var(--white)" stroke-width="2">
          <circle cx="12" cy="12" r="10"/><ellipse cx="12" cy="12" rx="4.5" ry="10"/><line x1="2" y1="12" x2="22" y2="12"/>
        </svg>
        <span>www.tkregulatoryadvisors.solutions</span>
      </div>
      <div class="footer-mail">
        <svg class="footer-icon" width="15" height="11" viewBox="0 0 24 18" aria-hidden="true">
          <rect x="0" y="0" width="24" height="18" fill="var(--white)"/>
          <polyline points="0,0 12,10 24,0" fill="none" stroke="var(--brand-blue)" stroke-width="2"/>
        </svg>
        <span>email@tkregulatoryadvisors.solutions</span>
      </div>
    </footer>
  </main>
</body>
</html>
```